Harrowgate Estates Business Card for Apartment Buildings

Create business cards for resident managers who run apartment buildings. The audience is the public who are searching for apartment rentals, and current residents who live at the apartment building. Key design element will be incorporating the company logo, however, the logo cannot dominate. The building name and manager name are more important than the logo. Current business card design leaves little room for copy, so we may need to reduce the size on the current card to allow for more space for copy.

Target Market(s)

Adults 18-65 years of age, who are looking for an apartment rental, plus current residents who live at our apartment buildings.

Industry/Entity Type

Property Management

Contact Information for Business Card

A major design element will be use of the company logo. Important property and manager contact information must be part of the design. The size of the logo will need to be reduced to make room for building and manager contact copy.

Font styles to use
Sans Serif

Colors
3176b5
000000
959595
ffffff

Requirements
Must have
• 1) Incorporate the company logo.
• 2) Use the company colors (dark blue, black/grey, over white).
• 3) FEATURE THE BUILDING NAME
• 4) FEATURE THE MANAGER NAME
• 5) The company name is less important than BUILDING and MANAGER
• 6) Manager contact information
• **SEE ATTACHED CREATIVE BRIEF**
Nice to have
• 1) Back of card logo watermark
• 2) Ability to write notes on back of carfd
Should not have
• Avoid letting the company logo dominate the card, the building name and manager are more important than the company logo.

```html
<!DOCTYPE html>
<html lang="en">
<head>
<meta charset="utf-8">
<title>Harrowgate Estates Business Card</title>
<link href="https://fonts.googleapis.com/css2?family=Work+Sans:wght@400;500;600;700&display=swap" rel="stylesheet">
<style>
  :root {
    --brand-blue: #3176b5;
    --card-black: #262626;
    --stage: #141414;
    --grey: #959595;
    --white: #ffffff;
  }
  * { margin: 0; padding: 0; box-sizing: border-box; }
  html, body {
    width: 1200px; height: 900px; overflow: hidden;
    background: var(--stage);
    font-family: "Work Sans", Arial, sans-serif;
  }
  .stage {
    width: 1200px; height: 900px;
    display: flex; flex-direction: column; align-items: center; justify-content: center; gap: 34px;
  }
  .card {
    position: relative;
    width: 700px; height: 400px;
    background: var(--card-black);
    border-bottom: 8px solid var(--brand-blue);
    overflow: hidden;
  }
  /* front */
  .card-front { display: flex; flex-direction: column; align-items: center; justify-content: center; }
  .wordmark {
    display: flex; align-items: center; gap: 12px;
    font-weight: 700; text-transform: uppercase; line-height: 1;
    white-space: nowrap;
  }
  .wordmark-dot { width: 16px; height: 16px; border-radius: 50%; flex: none; }
  .wordmark-name { font-size: 34px; letter-spacing: 1px; }
  .card-front .wordmark { color: var(--grey); margin-bottom: 30px; }
  .card-front .wordmark-dot { background: var(--grey); }
  .card-front .website {
    position: absolute; bottom: 34px; left: 0; right: 0; text-align: center;
    color: var(--white); font-size: 17px; letter-spacing: 3px;
  }
  .accent { color: var(--brand-blue); }
  /* back */
  .card-back { display: flex; align-items: center; }
  .back-brand { width: 330px; display: flex; justify-content: center; padding: 0 20px; }
  .card-back .wordmark { color: var(--white); }
  .card-back .wordmark-dot { background: var(--brand-blue); width: 14px; height: 14px; }
  .card-back .wordmark-name { font-size: 20px; }
  .divider { width: 2px; height: 270px; background: var(--brand-blue); flex: none; }
  .manager-info { padding-left: 34px; color: var(--white); }
  .manager-name {
    color: var(--brand-blue); font-size: 24px; font-weight: 600;
    letter-spacing: 1.5px; text-transform: uppercase;
  }
  .manager-title { font-size: 16px; letter-spacing: 1px; margin-bottom: 10px; }
  .building-name {
    color: var(--brand-blue); font-size: 16px; font-weight: 500;
    text-transform: uppercase; letter-spacing: 0.5px;
  }
  .address { font-size: 16px; letter-spacing: 1px; line-height: 1.3; margin-bottom: 12px; }
  .contact-list { list-style: none; }
  .contact-list li {
    display: flex; align-items: center; gap: 14px;
    font-size: 16px; letter-spacing: 1px; line-height: 1.7;
  }
  .contact-list svg { width: 15px; height: 15px; fill: var(--brand-blue); flex: none; }
</style>
</head>
<body>
<main class="stage">
  <section class="card card-front">
    <div class="wordmark">
      <span class="wordmark-dot"></span>
      <span class="wordmark-name">Harrowgate Estates LLC</span>
    </div>
    <p class="website">www.<span class="accent">harrowgateest</span>.com</p>
  </section>

  <section class="card card-back">
    <div class="back-brand">
      <div class="wordmark">
        <span class="wordmark-dot"></span>
        <span class="wordmark-name">Harrowgate Estates</span>
      </div>
    </div>
    <div class="divider"></div>
    <div class="manager-info">
      <h1 class="manager-name">Marisol Delgado</h1>
      <p class="manager-title">Resident Manager</p>
      <h2 class="building-name">Cedar Ridge Apartments</h2>
      <p class="address">2840 Linden Avenue<br>Millbrook, CA 95555</p>
      <ul class="contact-list">
        <li><svg viewBox="0 0 16 16" aria-hidden="true"><path d="M3 1l3 3-1.5 2a9 9 0 0 0 5.5 5.5L12 10l3 3-2 2C7 15 1 9 1 3z"/></svg><span>555-210-4471</span></li>
        <li><svg viewBox="0 0 16 16" aria-hidden="true"><path d="M4 1h8v4H4zM1 6h14v6h-3v3H4v-3H1zM5 10v4h6v-4z"/></svg><span>555-210-4472</span></li>
        <li><svg viewBox="0 0 16 16" aria-hidden="true"><path d="M4 0h8a1 1 0 0 1 1 1v14a1 1 0 0 1-1 1H4a1 1 0 0 1-1-1V1a1 1 0 0 1 1-1zm1 2v10h6V2zm3 11a1 1 0 1 0 0 2 1 1 0 0 0 0-2z"/></svg><span>555-386-9105</span></li>
        <li><svg viewBox="0 0 16 16" aria-hidden="true"><path d="M1 3h14v10H1zm1.5 1.2L8 8.5l5.5-4.3z"/></svg><span>marisol@harrowgateest.com</span></li>
        <li><svg viewBox="0 0 16 16" aria-hidden="true"><path d="M8 0a8 8 0 1 0 0 16A8 8 0 0 0 8 0zm-1 1.6C5.7 3 5 5 5 7H1.7A6.4 6.4 0 0 1 7 1.6zm2 0A6.4 6.4 0 0 1 14.3 7H11c0-2-.7-4-2-5.4zM6.5 7C6.6 5 7.1 3.2 8 2c.9 1.2 1.4 3 1.5 5zm-4.8 2H5c0 2 .7 4 2 5.4A6.4 6.4 0 0 1 1.7 9zm4.8 0h3c-.1 2-.6 3.8-1.5 5-.9-1.2-1.4-3-1.5-5zm4.5 0h3.3A6.4 6.4 0 0 1 9 14.4C10.3 13 11 11 11 9z"/></svg><span>www.<span class="accent">harrowgateest</span>.com</span></li>
      </ul>
    </div>
  </section>
</main>
</body>
</html>
```